Logo & Visitenkarte für KochWinkelhof
Zielgruppe
Die Jausenstation mit Hausmannskost
Aufgabenstellung
Telefonnummer 0517 649013
E-Mail kochwinkelhof@postfach-beispiel.at
Und den Firmennamen

```html
<!DOCTYPE html>
<html lang="de">
<head>
<meta charset="utf-8">
<title>KochWinkelhof – Visitenkarte</title>
<link href="https://fonts.googleapis.com/css2?family=Oswald:wght@300&display=swap" rel="stylesheet">
<style>
  :root {
    --backdrop: #c9cfd2;
    --card: #f7f7f7;
    --ink: #111111;
    --ring: #555555;
    --lime: #afba1d;
  }
  html, body {
    margin: 0;
    padding: 0;
    width: 1200px;
    height: 1200px;
    overflow: hidden;
    background: var(--backdrop);
    font-family: "Oswald", "Arial Narrow", sans-serif;
    font-weight: 300;
  }
  .card {
    position: absolute;
    left: 250px;
    width: 700px;
    height: 400px;
    background: var(--card);
  }
  .card--front { top: 147px; }
  .card--back  { top: 652px; }

  .brand-mark {
    position: absolute;
    left: 0;
    right: 0;
    top: 158px;
    display: flex;
    align-items: center;
    justify-content: center;
    gap: 18px;
  }
  .brand-mark__circle {
    width: 72px;
    height: 72px;
    border: 4px solid var(--ring);
    border-radius: 50%;
    box-sizing: border-box;
  }
  .brand-mark__name {
    font-size: 60px;
    line-height: 1;
    color: var(--ink);
    letter-spacing: 0.5px;
  }

  .contact {
    position: absolute;
    left: 47px;
    top: 150px;
    width: 420px;
  }
  .contact__name {
    margin: 0;
    font-size: 38px;
    line-height: 1;
    color: var(--lime);
    font-weight: 300;
  }
  .contact__tagline {
    margin: 20px 0 0;
    font-size: 21px;
    line-height: 1;
    color: var(--ink);
    text-transform: uppercase;
    letter-spacing: 0.2px;
  }
  .contact__rule {
    margin: 24px 0 0;
    width: 415px;
    height: 1px;
    border: 0;
    background: var(--lime);
  }
  .contact__row {
    display: flex;
    align-items: center;
    margin-top: 16px;
    font-size: 17px;
    color: var(--ink);
  }
  .contact__row + .contact__row { margin-top: 18px; }
  .contact__icon {
    width: 26px;
    height: 22px;
    margin-right: 13px;
    fill: var(--ink);
  }
  .contact__email { text-transform: uppercase; }
</style>
</head>
<body>

  <section class="card card--front">
    <div class="brand-mark">
      <div class="brand-mark__circle"></div>
      <div class="brand-mark__name">KochWinkelhof</div>
    </div>
  </section>

  <section class="card card--back">
    <div class="contact">
      <h1 class="contact__name">KochWinkelhof</h1>
      <p class="contact__tagline">Die Jausenstation mit Hausmannskost</p>
      <hr class="contact__rule">
      <div class="contact__row">
        <svg class="contact__icon" viewBox="0 0 24 24" aria-hidden="true">
          <path d="M6.6 10.8c1.4 2.8 3.8 5.1 6.6 6.6l2.2-2.2c.3-.3.7-.4 1-.2 1.1.4 2.3.6 3.6.6.6 0 1 .4 1 1V20c0 .6-.4 1-1 1C10.6 21 3 13.4 3 4c0-.6.4-1 1-1h3.5c.6 0 1 .4 1 1 0 1.3.2 2.5.6 3.6.1.3 0 .7-.2 1z"/>
        </svg>
        <span>0517 649013</span>
      </div>
      <div class="contact__row">
        <svg class="contact__icon" viewBox="0 0 26 20" aria-hidden="true">
          <path d="M1 2h24v2L13 11 1 4z"/>
          <path d="M1 6.3l12 7 12-7V18H1z"/>
        </svg>
        <span class="contact__email">kochwinkelhof@postfach-beispiel.at</span>
      </div>
    </div>
  </section>

</body>
</html>
```